Velmora health leaflet

We are looking for a new brand identity for our clinic to start with a new leaflet for communication. For current brand identity please look at our website Www.velmorahealth.cz. We would like to use less of the blue but more of the green turquoise and white. The logo should remain. See attached. We received few ideas but not sure about them. The design should be elegant and simple. Premium
#729694 Hex Color Code
The hexadecimal color code #729694 is a shade of cyan. In the RGB color model #729694 is composed of 44.71% red, 58.82% green and 58.04% blue. In the HSL color space #729694 has a hue of 177° (degrees), 15% saturation and 52% lightness. This color has an approximate wavelength of 492.66 nm.
Main headlines
Playfair Display
Serif, elegant
Body & UI
Lato
Clean, modern
Look and feel
Each slider illustrates characteristics of the customer's brand and the style your logo design should communicate.

```html
<!DOCTYPE html>
<html lang="en">
<head>
<meta charset="utf-8">
<title>Velmora Health leaflet</title>
<link href="https://fonts.googleapis.com/css2?family=Montserrat:wght@600;700;800&family=Overpass:wght@400;600;700&family=Lato:wght@400&display=swap" rel="stylesheet">
<style>
:root{
  --bg:#e3e3e3;
  --paper:#ffffff;
  --teal-deep:#0f8a8f;
  --teal:#27b3b8;
  --teal-text:#1aa1a6;
  --navy:#24486b;
  --ink:#1e2a2e;
  --label:#111111;
  --photo-a:#1f3a2a;
  --photo-b:#cfcfc9;
}
*{box-sizing:border-box;margin:0;padding:0}
html,body{width:1200px;height:904px;overflow:hidden;background:var(--bg)}
body{position:relative;font-family:"Overpass",sans-serif;color:var(--ink)}

.row{position:absolute;left:30px;width:1140px;height:340px}
.row--en{top:45px}
.row--cz{top:510px}

.page{position:absolute;top:0;width:240px;height:340px;background:var(--paper);overflow:hidden;box-shadow:0 8px 18px rgba(0,0,0,.18)}
.front{left:0}
.spread{position:absolute;left:300px;top:0;width:480px;height:340px;box-shadow:0 8px 18px rgba(0,0,0,.18);overflow:hidden;background:var(--paper)}
.back{left:840px;background:var(--teal)}

/* front */
.front__photo{position:absolute;left:0;top:0}
.brand{position:absolute;left:78px;top:150px;display:flex;align-items:center;gap:6px;font-family:"Montserrat",sans-serif;font-weight:700;font-size:15px;color:var(--ink)}
.brand__dot{width:7px;height:7px;border-radius:50%;background:var(--teal-text)}
.front__headline{position:absolute;left:22px;right:16px;top:190px;font-family:"Montserrat",sans-serif;font-weight:800;font-size:17px;line-height:1.12;text-align:center;color:var(--teal-text)}
.front__url{position:absolute;left:0;right:0;top:300px;text-align:center;font-family:"Montserrat",sans-serif;font-weight:600;font-size:8px;color:var(--teal-text)}

/* inside */
.inside__left{position:absolute;left:0;top:0;width:240px;height:198px;background:var(--teal-deep)}
.inside__right{position:absolute;left:240px;top:0;width:240px;height:198px;background:var(--teal)}
.inside__fold{position:absolute;left:239px;top:0;width:2px;height:340px;background:rgba(0,0,0,.06)}
.inside__title{position:absolute;left:38px;top:40px;width:180px;font-weight:700;font-size:15px;line-height:1.1;color:#fff}
.features{position:absolute;left:38px;top:120px;width:186px;list-style:disc;padding-left:8px;font-size:6px;line-height:1.45;color:#fff}
.about__title{position:absolute;left:20px;top:48px;width:150px;font-weight:700;font-size:12px;line-height:1.1;color:#fff}
.about__rule{position:absolute;left:20px;top:118px;width:30px;height:2px;background:#fff}
.about__text{position:absolute;left:20px;top:135px;width:196px;font-size:6px;line-height:1.5;color:#fff}
.inside__decor{position:absolute;right:0;top:6px}
.inside__photo{position:absolute;left:0;top:198px}

/* back */
.back__decor{position:absolute;left:0;top:0}
.contact{position:absolute;left:40px;top:48px;width:190px;color:#fff}
.contact__title{font-family:"Montserrat",sans-serif;font-weight:700;font-size:11px;margin:0 0 12px 20px}
.contact__line{display:flex;align-items:flex-start;gap:7px;font-family:"Montserrat",sans-serif;font-weight:600;font-size:7px;line-height:1.35;margin-bottom:6px}
.contact__note{font-family:"Montserrat",sans-serif;font-weight:700;font-size:7px;line-height:1.35;color:var(--navy);margin:2px 0 6px 0}
.icon{flex:0 0 12px;width:12px;height:12px;border-radius:50%;background:var(--navy);display:flex;align-items:center;justify-content:center}
.back__photo{position:absolute;left:0;bottom:0}

/* labels */
.labels{position:absolute;left:30px;top:410px;width:1140px;height:50px;font-family:"Lato",sans-serif;font-size:32px;letter-spacing:1px;color:var(--label)}
.label{position:absolute;top:0;text-align:center}
.label--front{left:0;width:240px}
.label--inside{left:300px;width:480px}
.label--back{left:840px;width:240px}
</style>
</head>
<body>

<svg width="0" height="0" style="position:absolute" aria-hidden="true">
  <defs>
    <linearGradient id="g-building" x1="0" y1="0" x2="1" y2="1">
      <stop offset="0" stop-color="#6f95c4"/><stop offset=".6" stop-color="#b7cbe0"/><stop offset="1" stop-color="#7f8f86"/>
    </linearGradient>
    <linearGradient id="g-team" x1="0" y1="0" x2="0" y2="1">
      <stop offset="0" stop-color="#1f3a2a"/><stop offset=".45" stop-color="#3c4a38"/><stop offset="1" stop-color="#e9e9e6"/>
    </linearGradient>
    <linearGradient id="g-lobby" x1="0" y1="0" x2="1" y2="1">
      <stop offset="0" stop-color="#e9eaea"/><stop offset=".55" stop-color="#cfd3d5"/><stop offset="1" stop-color="#9a6a45"/>
    </linearGradient>
  </defs>
</svg>

<!-- English row -->
<section class="row row--en">
  <article class="page front">
    <svg class="front__photo" width="240" height="160" role="img" aria-label="Photo of a modern glass office building">
      <path d="M0 0 H140 C132 70 82 122 0 152 Z" fill="url(#g-building)"/>
    </svg>
    <div class="brand"><span class="brand__dot"></span>Velmora Health</div>
    <h1 class="front__headline">World-class private health care in Prague is now only minutes away</h1>
    <p class="front__url">www.velmorahealth.cz</p>
  </article>

  <article class="spread">
    <div class="inside__left">
      <h2 class="inside__title">Explore<br>The Velmora<br>Difference</h2>
      <ul class="features">
        <li>We Treat You Like Family</li>
        <li>Trusted Personal Doctors</li>
        <li>Second Opinions and Virtual Consultations from International Top Doctors</li>
        <li>Center of Excellence for Lifestyle Medicine &amp; Healthy Longevity</li>
        <li>Manager Check-ups:<br>6 Hours, 6 Specialists</li>
        <li>Same or Next Day Appointments with Your Personal Doctor in acute cases (in person or virtual if desired)</li>
      </ul>
    </div>
    <div class="inside__right">
      <h2 class="about__title">About<br>Velmora Health<br>Europe, Your Private<br>Healthcare Clinic</h2>
      <div class="about__rule"></div>
      <p class="about__text">Today, fast access to a private doctor and a focus on the prevention of chronic disease is essential. We at Velmora Health Europe promise you same or next-day appointments with your private doctor, as well as 360° prevention and care, so you can stay healthy and live longer.</p>
      <svg class="inside__decor" width="80" height="90" aria-hidden="true">
        <path d="M44 2 A32 32 0 0 0 44 66" fill="none" stroke="var(--navy)" stroke-width="12"/>
        <circle cx="70" cy="60" r="20" fill="none" stroke="#fff" stroke-width="6"/>
      </svg>
    </div>
    <div class="inside__fold"></div>
    <svg class="inside__photo" width="480" height="142" role="img" aria-label="Group photo of the clinic's doctors in white coats">
      <path d="M14 142 C4 60 40 0 110 0 L330 0 C410 0 452 70 462 142 Z" fill="url(#g-team)"/>
    </svg>
  </article>

  <article class="page back">
    <svg class="back__decor" width="80" height="40" aria-hidden="true">
      <path d="M0 24 Q18 30 32 18" fill="none" stroke="#fff" stroke-width="6"/>
      <circle cx="56" cy="4" r="14" fill="none" stroke="var(--navy)" stroke-width="6"/>
    </svg>
    <div class="contact">
      <p class="contact__title">Contact us</p>
      <p class="contact__line"><span class="icon"><svg width="7" height="7" viewBox="0 0 10 10"><path d="M2 1 L4 3 L3 4.5 Q4.5 6.5 5.5 7 L7 6 L9 8 L7.5 9.5 Q2 8 0.5 2.5 Z" fill="#fff"/></svg></span>+420 200 555 010</p>
      <p class="contact__line"><span class="icon"><svg width="7" height="7" viewBox="0 0 10 10"><rect x="1" y="2" width="8" height="6" fill="none" stroke="#fff" stroke-width="1.2"/><path d="M1 2 L5 5.5 L9 2" fill="none" stroke="#fff" stroke-width="1.2"/></svg></span>team@velmorahealth.cz</p>
      <p class="contact__line"><span class="icon"><svg width="7" height="7" viewBox="0 0 10 10"><path d="M5 9.5 C2 6 1.5 4.5 1.5 3.5 A3.5 3.5 0 0 1 8.5 3.5 C8.5 4.5 8 6 5 9.5 Z" fill="#fff"/></svg></span>Lindenpark Office Korunní<br>118/4, 120 00 Praha 2</p>
      <p class="contact__note">Out of Hours Urgent Support for our Members ONLY:</p>
      <p class="contact__line"><span class="icon"><svg width="7" height="7" viewBox="0 0 10 10"><path d="M5 1 V6 M5 7.5 V9" stroke="#fff" stroke-width="1.6"/></svg></span>+420 700 555 021</p>
    </div>
    <svg class="back__photo" width="240" height="135" role="img" aria-label="Photo of the clinic reception desk">
      <path d="M0 135 L0 95 C20 30 90 0 170 4 L240 10 L240 135 Z" fill="url(#g-lobby)"/>
    </svg>
  </article>
</section>

<div class="labels">
  <span class="label label--front">FRONT</span>
  <span class="label label--inside">INSIDE</span>
  <span class="label label--back">BACK</span>
</div>

<!-- Czech row -->
<section class="row row--cz" lang="cs">
  <article class="page front">
    <svg class="front__photo" width="240" height="160" role="img" aria-label="Fotografie moderní prosklené kancelářské budovy">
      <path d="M0 0 H140 C132 70 82 122 0 152 Z" fill="url(#g-building)"/>
    </svg>
    <div class="brand"><span class="brand__dot"></span>Velmora Health</div>
    <h1 class="front__headline">Špičková lékařská péče v Praze jen pár minut od vás</h1>
    <p class="front__url">www.velmorahealth.cz</p>
  </article>

  <article class="spread">
    <div class="inside__left">
      <h2 class="inside__title">Zjistěte,<br>čím se Velmora<br>Health odlišuje</h2>
      <ul class="features">
        <li>Pečujeme o vás jako o vlastní rodinu</li>
        <li>Spolehliví osobní lékaři</li>
        <li>Posouzení navrhované léčby od dalšího specialisty a virtuální konzultace s nejlepšími mezinárodními lékaři</li>
        <li>Centrum excelence pro Lifestyle Medicine and Healthy Longevity</li>
        <li>Lékařské prohlídky pro manažery:<br>6 hodin, 6 specialistů</li>
        <li>Vyšetření u vašeho osobního lékaře v den objednání či následující den v akutních případech (osobně nebo virtuálně dle vašeho přání)</li>
      </ul>
    </div>
    <div class="inside__right">
      <h2 class="about__title">O společnosti<br>Velmora Health<br>Europe</h2>
      <div class="about__rule"></div>
      <p class="about__text">Rychlý přístup k osobnímu lékaři a zaměření na prevenci chronických onemocnění jsou v dnešní době naprosto nezbytné. Společnost Velmora Health Europe vám garantuje vyšetření u vašeho osobního lékaře v den objednání či nejpozději následující den. V rámci programu 360° Prevention and Care poskytujeme tu nejlepší lékařskou péči a prevenci pro vaše pevné zdraví a dlouhý život.</p>
      <svg class="inside__decor" width="80" height="90" aria-hidden="true">
        <path d="M44 2 A32 32 0 0 0 44 66" fill="none" stroke="var(--navy)" stroke-width="12"/>
        <circle cx="70" cy="60" r="20" fill="none" stroke="#fff" stroke-width="6"/>
      </svg>
    </div>
    <div class="inside__fold"></div>
    <svg class="inside__photo" width="480" height="142" role="img" aria-label="Skupinová fotografie lékařů kliniky v bílých pláštích">
      <path d="M14 142 C4 60 40 0 110 0 L330 0 C410 0 452 70 462 142 Z" fill="url(#g-team)"/>
    </svg>
  </article>

  <article class="page back">
    <svg class="back__decor" width="80" height="40" aria-hidden="true">
      <path d="M0 24 Q18 30 32 18" fill="none" stroke="#fff" stroke-width="6"/>
      <circle cx="56" cy="4" r="14" fill="none" stroke="var(--navy)" stroke-width="6"/>
    </svg>
    <div class="contact">
      <p class="contact__title">Kontaktujte nás</p>
      <p class="contact__line"><span class="icon"><svg width="7" height="7" viewBox="0 0 10 10"><path d="M2 1 L4 3 L3 4.5 Q4.5 6.5 5.5 7 L7 6 L9 8 L7.5 9.5 Q2 8 0.5 2.5 Z" fill="#fff"/></svg></span>+420 200 555 010</p>
      <p class="contact__line"><span class="icon"><svg width="7" height="7" viewBox="0 0 10 10"><rect x="1" y="2" width="8" height="6" fill="none" stroke="#fff" stroke-width="1.2"/><path d="M1 2 L5 5.5 L9 2" fill="none" stroke="#fff" stroke-width="1.2"/></svg></span>team@velmorahealth.cz</p>
      <p class="contact__line"><span class="icon"><svg width="7" height="7" viewBox="0 0 10 10"><path d="M5 9.5 C2 6 1.5 4.5 1.5 3.5 A3.5 3.5 0 0 1 8.5 3.5 C8.5 4.5 8 6 5 9.5 Z" fill="#fff"/></svg></span>Lindenpark Office Korunní<br>118/4, 120 00 Praha 2</p>
      <p class="contact__note">Naléhavá podpora mimo pracovní dobu pro členy:</p>
      <p class="contact__line"><span class="icon"><svg width="7" height="7" viewBox="0 0 10 10"><path d="M5 1 V6 M5 7.5 V9" stroke="#fff" stroke-width="1.6"/></svg></span>+420 700 555 021</p>
    </div>
    <svg class="back__photo" width="240" height="135" role="img" aria-label="Fotografie recepce kliniky">
      <path d="M0 135 L0 95 C20 30 90 0 170 4 L240 10 L240 135 Z" fill="url(#g-lobby)"/>
    </svg>
  </article>
</section>

</body>
</html>
```